Australian Legal Practice would like a Web Design

I need a web design for a newly established law practice operating as Brindell Legal.

I would like the business to have an internet presence (via a website) essentially for the purpose of marketing and advertising. As the business grows (hopefully) I may be interested in providing general legal information as a means of establishing goodwill in the community and a easy and user friends contact method through the website.

The essence of the business is personal legal service based on local knowledge and therefore i want the website to present a picture of friendly professionalism, but mostly i want people who to be able to find the contact details of the business

I would like to have a map of the office location, and photos of the front of the office, the staff (me at the moment) and picture of law themed items and featuring the Brindell Legal logo.

The areas of law which Brindell Legal practises in are as follows:

commercial law
business sale and purchases
leases
conveyancing and property law
wills and estates
powers of attorney
general legal advice
succession planning
Updates

Target Market(s)

Potential and existing clients of the firm
Other law firms
Associated stakeholders, i.e. Banks and real estate agents

Industry/Entity Type

Law Firm

Coding

Coded - Design and coding required

Number of Pages Required

2 page

Font styles to use
Sans Serif

Colors
85acd3
33a6d7
0456a4

Requirements
Must have
• Brindell Legal logo
• Map of the office location
• Picture of Ross Kedwick (principal solicitor)
• Picture of the office
• Areas of Practice
• Address of office
• email address: ross.kedwick@brindelllegal-example.com.au
• Physical address: 17 Pellow Road, Hamilton VIC 3300
• Phone number: (03) 5598 4731
• Facsimile number: (03) 5598 4706
• Space for a brief description of the firm and its competitive advantage
• Bar Guild Logo
• Links to the Bar Guild of Victoria
• Link to the practitioner oversight Council
Nice to have
• coded to wordpress format

```html
<!DOCTYPE html>
<html lang="en">
<head>
<meta charset="utf-8">
<title>Brindell Legal</title>
<link href="https://fonts.googleapis.com/css2?family=Open+Sans:wght@400;600;700;800&display=swap" rel="stylesheet">
<style>
:root{
  --navy:#0e3d6b;
  --blue:#0456a4;
  --bright:#33a6d7;
  --sky:#85acd3;
  --accent:#1f8ed3;
  --ink:#333b44;
  --muted:#7a8590;
  --line:#e3e8ee;
  --panel:#f4f6f8;
  --dark:#1d1f22;
  --white:#ffffff;
}
*{margin:0;padding:0;box-sizing:border-box}
html,body{width:1200px;height:2256px;overflow:hidden}
body{font-family:"Open Sans",Arial,sans-serif;color:var(--ink);background:var(--white);position:relative;font-size:13px}
.abs{position:absolute}

/* top bar */
.topbar{top:0;left:0;width:1200px;height:34px;background:var(--navy);color:#cfe0f0;font-size:12px}
.topbar .mail{left:80px;top:9px;display:flex;gap:8px;align-items:center}
.topbar .meta{right:80px;top:9px;display:flex;gap:14px;align-items:center}
.topbar .sep{color:#5f84a8}

/* header */
.header{top:34px;left:0;width:1200px;height:76px;background:var(--white);border-bottom:1px solid var(--line)}
.logo{left:80px;top:20px;display:flex;align-items:center;gap:10px;font-size:30px;font-weight:800;color:var(--blue);letter-spacing:1px}
.logo .mark{width:22px;height:22px;background:var(--bright)}
.nav{right:80px;top:0;display:flex;height:76px}
.nav a{display:flex;align-items:center;padding:0 20px;font-size:13px;font-weight:600;color:var(--ink);text-decoration:none}
.nav a.active{background:#e9f4fb;color:var(--accent);border-top:3px solid var(--accent)}

/* hero */
.hero{top:110px;left:0;width:1200px;height:530px;background:linear-gradient(120deg,#c9c3bb 0%,#8c8f94 35%,#3f4f63 60%,#a4a7ab 100%)}
.hero .arrow{top:240px;width:38px;height:38px;border-radius:50%;background:rgba(255,255,255,.85)}
.hero-title{left:700px;top:386px;font-size:54px;font-weight:800;color:var(--white);letter-spacing:1px}
.hero-band{left:700px;top:462px;width:500px;height:40px;background:var(--accent);color:var(--white);font-size:18px;padding:8px 24px}

/* welcome */
.welcome{top:680px;left:60px;width:1080px;height:390px;background:var(--panel)}
.welcome-photo{left:80px;top:720px;width:280px;height:310px;background:linear-gradient(160deg,#dfe4ea,#6f7b8a)}
.welcome-text{left:400px;top:716px;width:720px}
.welcome-text h2{font-size:24px;font-weight:700;color:var(--ink);margin-bottom:16px}
.welcome-text h2 span{color:var(--accent)}
.welcome-text p{font-size:13px;line-height:21px;color:var(--muted);margin-bottom:16px}
.btn{display:inline-block;background:var(--blue);color:var(--white);font-size:12px;font-weight:600;padding:7px 18px;border-radius:3px}

/* practice */
.practice{top:1100px;left:0;width:1200px;height:410px;background:linear-gradient(180deg,#0b4f90,#0456a4 60%,#0a3f73)}
.practice h2{position:absolute;top:52px;width:1200px;text-align:center;color:var(--white);font-size:26px;font-weight:700}
.practice .rule{top:96px;left:570px;width:60px;height:3px;background:var(--bright)}
.practice .side{top:220px;width:30px;height:30px;border-radius:50%;border:2px solid rgba(255,255,255,.6)}
.area{top:140px;width:220px;text-align:center;color:var(--white)}
.area .icon{width:64px;height:64px;border-radius:50%;background:var(--white);margin:0 auto 18px;display:flex;align-items:center;justify-content:center}
.area h3{font-size:14px;font-weight:700;margin-bottom:8px}
.area p{font-size:11.5px;line-height:17px;color:#cfe0f0;margin-bottom:18px}
.area .btn{background:#e9edf2;color:var(--ink)}

/* gallery & news */
.sec-title{font-size:18px;font-weight:700;color:var(--accent)}
.gallery{left:80px;top:1560px}
.grid{left:80px;top:1600px;display:grid;grid-template-columns:repeat(3,150px);grid-auto-rows:110px;gap:10px}
.grid div{background:linear-gradient(135deg,#c6ccd4,#5d6b7c)}
.news{left:660px;top:1560px}
.news-item{left:660px;width:460px;display:flex;gap:18px}
.news-item .thumb{width:160px;height:110px;background:linear-gradient(135deg,#dfe3e8,#8896a6);flex:none}
.news-item h4{font-size:13px;color:var(--accent);font-weight:700;margin-bottom:4px}
.news-item .date{font-size:11px;color:var(--muted);margin-bottom:6px}
.news-item p{font-size:11.5px;line-height:17px;color:var(--muted);margin-bottom:6px}
.news-item .more{font-size:11px;color:var(--accent);font-weight:600}

/* footer */
.footer{top:1996px;left:0;width:1200px;height:200px;background:var(--accent);color:var(--white)}
.footer h5{font-size:13px;font-weight:700;margin-bottom:14px}
.col{top:26px}
.col ul{list-style:none;font-size:11px;line-height:20px;color:#e3f1fb}
.col p{font-size:11px;line-height:20px;color:#e3f1fb}
.map{width:180px;height:100px;background:linear-gradient(135deg,#e7ecef,#c1cfd8)}
.sub{display:flex;margin-top:10px}
.sub span{width:150px;height:26px;background:var(--white);color:#9aa;font-size:11px;padding:5px 8px}
.sub b{height:26px;background:var(--navy);font-size:11px;padding:5px 10px;font-weight:600}
.social{display:flex;gap:10px;margin-top:14px}
.social i{width:26px;height:26px;border-radius:50%;background:rgba(255,255,255,.25)}
.bottombar{top:2196px;left:0;width:1200px;height:60px;background:var(--dark);color:#b8bcc2;font-size:11px;text-align:center;padding-top:22px}
</style>
</head>
<body>

<div class="topbar abs">
  <div class="mail abs">
    <svg width="14" height="10" viewBox="0 0 14 10"><rect x=".5" y=".5" width="13" height="9" fill="none" stroke="#cfe0f0"/><path d="M.5 .5 7 6 13.5 .5" fill="none" stroke="#cfe0f0"/></svg>
    ross.kedwick@brindelllegal-example.com.au
  </div>
  <div class="meta abs">
    <span>(03) 5598 4731</span><span class="sep">|</span>
    <span>17 Pellow Road, Dunmarra VIC 3391</span><span class="sep">|</span>
    <span>LOG IN</span>
  </div>
</div>

<header class="header abs">
  <div class="logo abs"><span class="mark"></span>BRINDELL LEGAL</div>
  <nav class="nav abs">
    <a class="active">HOME</a><a>ABOUT US</a><a>AREAS OF PRACTICE</a><a>NEWS</a><a>CONTACT US</a>
  </nav>
</header>

<section class="hero abs" role="img" aria-label="Photo of the principal solicitor with colleagues in business attire">
  <div class="arrow abs" style="left:40px"></div>
  <div class="arrow abs" style="right:40px"></div>
  <div class="hero-title abs">BRINDELL LEGAL</div>
  <div class="hero-band abs">Lorem Ipsum is simply dummy text</div>
</section>

<div class="welcome abs"></div>
<div class="welcome-photo abs" role="img" aria-label="Photo of Ross Kedwick, principal solicitor, in the office"></div>
<div class="welcome-text abs">
  <h2>WELCOME TO <span>BRINDELL LEGAL</span></h2>
  <p>Lorem Ipsum is simply dummy text of the printing and typesetting industry. Lorem Ipsum has been the industry's standard dummy text ever since the 1500s, when an unknown printer took a galley of type and scrambled it to make a type specimen book. It has survived not only five centuries, but also the leap into electronic typesetting, remaining essentially unchanged. It was popularised in the desktop publishing software like Aldus PageMaker including versions of Lorem Ipsum.</p>
  <p>Lorem Ipsum is simply dummy text of the printing and typesetting industry. Lorem Ipsum has been the industry's standard dummy text ever since the 1500s, when an unknown printer took a galley of type and scrambled it to make a type specimen book. It has survived not only five centuries, but also the leap into electronic typesetting, remaining essentially unchanged.</p>
  <span class="btn">Read More</span>
</div>

<section class="practice abs">
  <h2>AREAS OF PRACTICE</h2>
  <div class="rule abs"></div>
  <div class="side abs" style="left:40px"></div>
  <div class="side abs" style="right:40px"></div>

  <div class="area abs" style="left:90px">
    <div class="icon"><svg width="30" height="26" viewBox="0 0 30 26"><rect x="2" y="7" width="26" height="17" rx="2" fill="#0456a4"/><rect x="10" y="2" width="10" height="6" rx="1" fill="none" stroke="#0456a4" stroke-width="2"/></svg></div>
    <h3>COMMERCIAL LAW</h3>
    <p>Lorem Ipsum has been the industry's standard dummy text ever since the 1500s.</p>
    <span class="btn">Read More</span>
  </div>
  <div class="area abs" style="left:350px">
    <div class="icon"><svg width="30" height="28" viewBox="0 0 30 28"><path d="M15 2 2 13h4v13h18V13h4z" fill="#0456a4"/></svg></div>
    <h3>LEASES</h3>
    <p>Lorem Ipsum has been the industry's standard dummy text ever since the 1500s.</p>
    <span class="btn">Read More</span>
  </div>
  <div class="area abs" style="left:620px">
    <div class="icon"><svg width="24" height="30" viewBox="0 0 24 30"><path d="M2 2h14l6 6v20H2z" fill="#0456a4"/><path d="M6 14h12M6 19h12M6 24h8" stroke="#fff" stroke-width="2"/></svg></div>
    <h3>WILLS AND ESTATES</h3>
    <p>Lorem Ipsum has been the industry's standard dummy text ever since the 1500s.</p>
    <span class="btn">Read More</span>
  </div>
  <div class="area abs" style="left:890px">
    <div class="icon"><svg width="30" height="30" viewBox="0 0 30 30"><rect x="6" y="4" width="14" height="8" rx="1" transform="rotate(-40 13 8)" fill="#0456a4"/><path d="M15 13 26 25" stroke="#0456a4" stroke-width="3"/><rect x="3" y="24" width="14" height="3" fill="#0456a4"/></svg></div>
    <h3>POWERS OF ATTORNEY</h3>
    <p>Lorem Ipsum has been the industry's standard dummy text ever since the 1500s.</p>
    <span class="btn">Read More</span>
  </div>
</section>

<div class="gallery abs sec-title">GALLERY</div>
<div class="grid abs" role="img" aria-label="Gallery of photos of the office front, meeting rooms and law themed items">
  <div></div><div></div><div></div><div></div><div></div><div></div><div></div><div></div><div></div>
</div>

<div class="news abs sec-title">LATEST NEWS</div>
<div class="news-item abs" style="top:1600px">
  <div class="thumb" role="img" aria-label="Photo of a client meeting"></div>
  <div>
    <h4>Neque Quis Ipsum Tellus</h4>
    <div class="date">24.02.2015</div>
    <p>Lorem Ipsum has been the industry's standard dummy text ever since the 1500s, when an unknown printer took a galley of type.</p>
    <span class="more">Read More »</span>
  </div>
</div>
<div class="news-item abs" style="top:1740px">
  <div class="thumb" role="img" aria-label="Photo of signing legal documents"></div>
  <div>
    <h4>Neque Quis Ipsum Tellus</h4>
    <div class="date">24.02.2015</div>
    <p>Lorem Ipsum has been the industry's standard dummy text ever since the 1500s, when an unknown printer took a galley of type.</p>
    <span class="more">Read More »</span>
  </div>
</div>

<footer class="footer abs">
  <div class="col abs" style="left:80px">
    <h5>LINKS</h5>
    <ul><li>› Customer Support</li><li>› Terms &amp; Conditions</li><li>› Disclaimer</li><li>› Bar Guild</li><li>› Privacy Policy</li></ul>
  </div>
  <div class="col abs" style="left:250px">
    <h5>LOCATION</h5>
    <div class="map" role="img" aria-label="Map of the office location on Pellow Road"></div>
  </div>
  <div class="col abs" style="left:590px">
    <h5>GET IN TOUCH</h5>
    <p>Address: 17 Pellow Road, Dunmarra VIC 3391</p>
    <p>Phone: (03) 5598 4731</p>
    <p>Fax: (03) 5598 4706</p>
    <p>Email: ross.kedwick@brindelllegal-example.com.au</p>
  </div>
  <div class="col abs" style="left:900px">
    <h5>NEWSLETTER</h5>
    <p>Sign up to our newsletter to stay up to date with local news.</p>
    <div class="sub"><span>Email address</span><b>Submit</b></div>
    <div class="social"><i></i><i></i><i></i></div>
  </div>
</footer>

<div class="bottombar abs">Copyright © 2015. All Rights Reserved.</div>

</body>
</html>
```